Website Design for a New Business Sharing Application

Purpose: Website for a new product – a sharing application called "Tavrelo.to"

Product concept: Easy sharing of business information. The application has different sections: tasks, calendars, documents, contacts, notes and links. The key feature of the application is that you can drag and drop information from different sections into a "share." A share is a page which lists all the types of information that you drag into it. You can add people to this "share."

Note: The application itself is not part of this project, just the website.

Website details: The site, in addition to being informational, will actually be the first point of entry for visitors into the application itself. Because of that, we would like the website design to reflect the look of the application, to create a smooth and seamless experience for the user moving from the website into the application (tough the website does not need to look *exactly* like the application). Included Product Tour screenshots show you the look of the application.

Website pages to be created: 4 pages
We are flexible in terms of the exact structure and placement of elements. You may change that any way you like. The pages are as follows:

Home page
Product Tour page
Press page
Blog page

Specific description of pages are provided in project files we will upload. We will also upload the logo, home page layout we have in mind, and other supporting files.

NOTE: Please submit first the design of the home page. Based on this design we will ask selected designers to submit designs for the other pages.

Target Market(s)

Business people who want to share work related files with their colleagues

Industry/Entity Type

Business

Requirements
Must have
• All the required features are listed in the description of the website and specific pages that we will upload.

```html
<!DOCTYPE html>
<html lang="en">
<head>
<meta charset="utf-8">
<title>Tavrelo.to – Share Now</title>
<link rel="stylesheet" href="https://fonts.googleapis.com/css2?family=Roboto+Condensed:wght@300;400;700&family=Oswald:wght@700&family=Arimo:wght@400;700&display=swap">
<style>
  :root{
    --sky:#03a4e1;
    --topbar:#f4f5f6;
    --white:#ffffff;
    --nav-text:#1a6eae;
    --tab-top:#5cc3f2;
    --tab-bottom:#0b8fd3;
    --orange-top:#ffb23a;
    --orange-bottom:#d8660a;
    --ink:#0d1a22;
    --footer:#0a6e97;
    --footer-link:#a6e3ff;
    --icon:#eaf7ff;
    --field:#eeeeee;
    --field-text:#444444;
    --deep-btn:#0f5d84;
    --brand-dot:#e8771c;
  }
  *{box-sizing:border-box;margin:0;padding:0}
  html,body{width:1200px;height:835px;overflow:hidden;background:var(--sky)}
  body{font-family:"Arimo",Arial,sans-serif;position:relative}
  .page{position:relative;width:1200px;height:835px;overflow:hidden;background:var(--sky)}

  /* header */
  .topbar{position:absolute;left:0;top:0;width:1200px;height:72px;background:var(--topbar)}
  .brand-cap{position:absolute;left:78px;top:-40px;width:247px;height:148px;border-radius:50%;background:var(--white)}
  .brand{position:absolute;left:112px;top:26px;display:flex;align-items:center;gap:9px;
    font-family:"Roboto Condensed",sans-serif;font-weight:700;font-size:31px;color:var(--nav-text)}
  .brand-dot{width:24px;height:24px;border-radius:50%;background:var(--brand-dot)}
  .nav{position:absolute;left:448px;top:24px;display:flex;font-family:"Roboto Condensed",sans-serif;font-size:19px}
  .nav a{display:block;height:48px;line-height:46px;padding:0 19px;color:var(--nav-text);text-decoration:none;margin-right:7px}
  .nav a.is-current{color:var(--white);background:linear-gradient(var(--tab-top),var(--tab-bottom));border-radius:4px 4px 0 0;border:1px solid #1580c0;border-bottom:0}
  .access-btn{position:absolute;left:928px;top:20px;width:154px;height:34px;border-radius:17px;
    background:linear-gradient(#5ccdf7,#0d7fc2);box-shadow:0 2px 0 #0a5a8e;
    color:var(--white);font-family:"Roboto Condensed",sans-serif;font-size:15px;text-align:center;line-height:33px}

  /* hero */
  .hero-glow{position:absolute;left:300px;top:72px;width:600px;height:230px;
    background:radial-gradient(ellipse at center,rgba(255,255,255,.18),rgba(255,255,255,0) 70%)}
  .hero-title{position:absolute;left:0;top:90px;width:1200px;text-align:center;
    font-family:"Oswald",sans-serif;font-weight:700;font-size:44px;letter-spacing:1px;line-height:1;
    color:#ff9a1e;text-shadow:0 2px 2px rgba(0,60,100,.35)}
  .hero-sub{position:absolute;left:0;top:158px;width:1200px;text-align:center;
    font-family:"Roboto Condensed",sans-serif;font-size:21px;color:var(--ink)}
  .kinds{position:absolute;left:0;top:201px;width:1200px;height:70px}
  .kind{position:absolute;top:0;width:90px;margin-left:-45px;text-align:center;
    font-family:"Roboto Condensed",sans-serif;font-size:16px;color:#103b55}
  .kind svg{display:block;margin:0 auto 14px;width:30px;height:30px}

  /* action deck */
  .deck{position:absolute;left:0;top:270px;width:1200px;height:120px}
  .field{position:absolute;top:30px;width:447px;height:49px;border-radius:25px;background:var(--white);
    box-shadow:0 2px 3px rgba(0,50,90,.3)}
  .field-input{position:absolute;left:4px;top:4px;right:4px;bottom:4px;border-radius:21px;background:var(--field);
    font-family:"Roboto Condensed",sans-serif;font-size:17px;color:var(--field-text);line-height:41px;padding-left:32px}
  .field-btn{position:absolute;right:4px;top:4px;width:116px;height:41px;border-radius:0 21px 21px 0;
    background:linear-gradient(var(--orange-top),var(--orange-bottom));
    color:var(--white);font-family:"Roboto Condensed",sans-serif;font-size:20px;text-align:center;line-height:41px}
  .field--upload{left:107px}
  .field--signup{left:635px}
  .field--signup .field-btn{width:126px}

  /* content panel */
  .panel{position:absolute;left:38px;top:382px;width:1114px;height:372px;
    background:linear-gradient(#26b2e8,#12a8e2 40%,var(--sky))}
  .how-title{position:absolute;left:106px;top:402px;font-family:"Roboto Condensed",sans-serif;font-weight:400;font-size:38px;color:var(--white)}
  .how-rule{position:absolute;left:107px;top:456px;width:497px;height:1px;background:#0d7db2;border-bottom:1px solid #5dcaf3}
  .how-text{position:absolute;left:107px;top:470px;width:478px;font-size:12.3px;line-height:23px;color:var(--ink)}
  .read-more{position:absolute;left:477px;top:659px;width:104px;height:30px;border-radius:15px;
    background:linear-gradient(#2c8db9,var(--deep-btn));box-shadow:0 2px 2px rgba(0,40,70,.4);
    color:var(--white);font-weight:700;font-size:12px;text-align:center;line-height:30px}
  .video{position:absolute;left:644px;top:412px;width:439px;height:315px;background:var(--white);padding:4px;
    box-shadow:0 2px 4px rgba(0,40,70,.3)}
  .video-screen{position:relative;width:100%;height:100%;
    background:linear-gradient(135deg,#7b5a46,#3e4652 45%,#8a6a62 70%,#2b2f36)}
  .video-play{position:absolute;left:50%;top:50%;width:56px;height:56px;margin:-34px 0 0 -28px;border-radius:50%;background:rgba(0,0,0,.65)}
  .video-play svg{position:absolute;left:19px;top:16px}
  .video-bar{position:absolute;left:0;right:0;bottom:0;height:28px;background:#151515;border-top:3px solid #d11}

  /* footer */
  .footer{position:absolute;left:0;top:754px;width:1200px;height:48px;background:var(--footer)}
  .footer-links{position:absolute;left:107px;top:16px;font-size:13px;color:var(--footer-link)}
  .footer-links a{color:var(--footer-link);text-decoration:none}
  .footer-links i{font-style:normal;color:#dff4ff;margin:0 6px}
  .social{position:absolute;left:980px;top:14px;display:flex;gap:7px}
  .social span{width:20px;height:20px;border-radius:3px;background:linear-gradient(#4cc6f5,#1188c6);box-shadow:0 1px 0 #064e70}
</style>
</head>
<body>
<div class="page">

  <header>
    <div class="topbar"></div>
    <div class="brand-cap"></div>
    <div class="brand"><span class="brand-dot"></span>Tavrelo.to</div>
    <nav class="nav">
      <a href="#" class="is-current">Home</a>
      <a href="#">Product Tour</a>
      <a href="#">Press</a>
      <a href="#">Blog</a>
    </nav>
    <a class="access-btn">Access your shares</a>
  </header>

  <section class="hero">
    <div class="hero-glow"></div>
    <h1 class="hero-title">SHARE NOW</h1>
    <p class="hero-sub">Drag information, add people, BOOM!</p>

    <div class="kinds">
      <div class="kind" style="left:366px">
        <svg viewBox="0 0 32 32" fill="none" stroke="var(--icon)" stroke-width="2"><rect x="4" y="6" width="24" height="6" rx="1"/><rect x="4" y="14" width="24" height="6" rx="1"/><rect x="4" y="22" width="24" height="6" rx="1"/></svg>
        <span>Files</span>
      </div>
      <div class="kind" style="left:439px">
        <svg viewBox="0 0 32 32" fill="none" stroke="var(--icon)" stroke-width="2"><rect x="3" y="9" width="26" height="18" rx="2"/><path d="M11 9l2-4h6l2 4"/><circle cx="16" cy="18" r="5"/></svg>
        <span>Pictures</span>
      </div>
      <div class="kind" style="left:516px">
        <svg viewBox="0 0 32 32" fill="none" stroke="var(--icon)" stroke-width="2"><rect x="8" y="4" width="18" height="24" rx="2"/><path d="M5 9h5M5 15h5M5 21h5M13 11h9M13 16h9"/></svg>
        <span>Tasks</span>
      </div>
      <div class="kind" style="left:586px">
        <svg viewBox="0 0 32 32" fill="none" stroke="var(--icon)" stroke-width="2"><path d="M3 9h9l2 3h15v15H3z"/><circle cx="16" cy="18" r="3"/><path d="M11 25c1-3 9-3 10 0"/></svg>
        <span>to-dos</span>
      </div>
      <div class="kind" style="left:674px">
        <svg viewBox="0 0 32 32" fill="none" stroke="var(--icon)" stroke-width="2"><rect x="3" y="6" width="26" height="22" rx="2"/><path d="M3 12h26M10 3v6M22 3v6M9 17h3M15 17h3M21 17h3M9 22h3M15 22h3M21 22h3"/></svg>
        <span>Calendars</span>
      </div>
      <div class="kind" style="left:756px">
        <svg viewBox="0 0 32 32" fill="none" stroke="var(--icon)" stroke-width="2"><path d="M22 4l6 6L12 26H6v-6z"/><path d="M19 7l6 6"/></svg>
        <span>Notes</span>
      </div>
      <div class="kind" style="left:825px">
        <svg viewBox="0 0 32 32" fill="none" stroke="var(--icon)" stroke-width="2.4"><path d="M14 18a5 5 0 0 0 7 0l5-5a5 5 0 0 0-7-7l-2 2"/><path d="M18 14a5 5 0 0 0-7 0l-5 5a5 5 0 0 0 7 7l2-2"/></svg>
        <span>Links</span>
      </div>
    </div>
  </section>

  <section class="deck">
    <svg width="1200" height="120" viewBox="0 0 1200 120" style="position:absolute;left:0;top:0">
      <defs>
        <linearGradient id="deckFill" x1="0" y1="0" x2="0" y2="1">
          <stop offset="0" stop-color="#1fb0e8"/>
          <stop offset="1" stop-color="#45c1ef"/>
        </linearGradient>
      </defs>
      <path d="M108 6 H1094 L1158 106 Q1160 112 1152 112 H40 Q31 112 34 106 Z" fill="url(#deckFill)"/>
      <path d="M34 107 H1158" stroke="#7fd6f6" stroke-width="2"/>
    </svg>
    <div class="field field--upload">
      <div class="field-input">Drag Files Here to Share Immediately</div>
      <div class="field-btn">Upload Files</div>
    </div>
    <div class="field field--signup">
      <div class="field-input">Enter your email address</div>
      <div class="field-btn">Start Sharing</div>
    </div>
  </section>

  <main>
    <div class="panel"></div>
    <h2 class="how-title">How it is work?</h2>
    <div class="how-rule"></div>
    <p class="how-text">The site, in addition to being informational, will actually be the first point of entry for visitors into the application itself. Because of that, we would like the website design to reflect the look of the application, to create a smooth and seamless experience for the user moving from the website into the application (tough the website does not need to look *exactly* like the application). Included Product Tour screenshots show you the look of the application.</p>
    <a class="read-more">READ MORE</a>

    <div class="video">
      <div class="video-screen" role="img" aria-label="Product video preview showing a collage of people sharing in everyday scenes">
        <div class="video-play"><svg width="22" height="24" viewBox="0 0 22 24"><path d="M2 2l18 10L2 22z" fill="#fff"/></svg></div>
        <div class="video-bar"></div>
      </div>
    </div>
  </main>

  <footer class="footer">
    <div class="footer-links">
      <a>Home</a><i>/</i><a>About us</a><i>/</i><a>Product Tour</a><i>/</i><a>Free for Unlimited users</a><i>/</i><a>Terms of use</a><i>/</i><a>Jobs</a><i>/</i><a>Sign up</a><i>/</i><a>Blog</a><i>/</i><a>Press</a><i>/</i><a>Contact us</a>
    </div>
    <div class="social" aria-label="Social links">
      <span></span><span></span><span></span><span></span>
    </div>
  </footer>

</div>
</body>
</html>
```